The Maplewood Kids Health Centre needs a Letterhead

We are a bilingual pediatric clinic located in Montreal, Canada.

Our english name is Maplewood Kids Health Centre
Our french name is Centre médical Bellerive

We offer complete care for children including general pediatric care, pediatric specialist care such as Ear, Nose and Throat, Urology, Neurology and Adolescent Medicine. We also have paramedical specialists such as psychologists, social workers, occupational therapists, speech and language pathologists.

The letterhead must use and be harmonious with our new logo. See Design #4923293. We need two types of letterhead. One for a the Logo and both english and french names on the top and the second with the list of current staff on the left. I have uploaded two old examples for you to see. Thanks and good luck.

Industry/Entity Type

Clinic

Font styles to use
Sans Serif

Colors
3176b5
9d9d9d

Requirements
Must have
• Include our logo.
Nice to have
• Most of our printing is done in black and white. So a grayscale design is fine.
I have included a color and grayscale versions of our logo.

We prefer clean modern designs.

```html
<!DOCTYPE html>
<html lang="fr">
<head>
<meta charset="utf-8">
<title>Letterhead – Maplewood Kids Health Centre</title>
<link href="https://fonts.googleapis.com/css2?family=Questrial&family=Source+Sans+3:wght@400;600&display=swap" rel="stylesheet">
<style>
  :root{
    --backdrop:#e9e6e2;
    --paper:#ffffff;
    --brand-blue:#5e74b3;
    --brand-purple:#5b3f7d;
    --heading:#5b6eaf;
    --ink:#222222;
    --rule:#9d9d9d;
  }
  *{margin:0;padding:0;box-sizing:border-box}
  html,body{width:1200px;height:774px;overflow:hidden;background:var(--backdrop)}
  .sheet{position:absolute;top:23px;width:571px;height:734px;background:var(--paper);
    box-shadow:0 1px 4px rgba(0,0,0,.35);overflow:hidden;font-family:"Source Sans 3",sans-serif;color:var(--ink)}
  .sheet--staff{left:17px}
  .sheet--plain{left:610px}

  .brand{position:absolute;top:19px;left:10px;display:flex;align-items:center;gap:10px;
    font-family:"Questrial",sans-serif;font-size:17.5px;line-height:20px;color:var(--brand-blue)}
  .brand__fr{text-align:right;width:88px}
  .brand__dot{width:14px;height:14px;border-radius:50%;background:var(--brand-blue)}
  .brand__en{text-align:left}

  .contact-top{position:absolute;top:33px;left:455px;border-left:1px solid var(--rule);
    padding-left:9px;font-size:10.5px;line-height:19px}
  .contact-line{display:flex;align-items:center;gap:5px}
  .icon{width:10px;height:10px;fill:var(--brand-blue)}

  .staff-column{position:absolute;top:152px;left:13px;font-size:10.5px;line-height:13.6px}
  .address{margin-bottom:8px}
  .staff-column .contact-line{line-height:18px}
  .dept{margin-top:12px}
  .dept__title{font-weight:600;color:var(--heading);font-size:10.5px;line-height:13px}
  .dept__names{font-size:8.5px;line-height:11.2px}

  .footer{position:absolute;left:0;bottom:0;width:571px;height:80px}
  .footer__address{position:absolute;left:0;right:0;bottom:6px;text-align:center;
    color:#fff;font-size:10.5px}
</style>
</head>
<body>

<section class="sheet sheet--staff">
  <header class="brand">
    <div class="brand__fr">Centre<br>médical<br>Bellerive</div>
    <div class="brand__dot"></div>
    <div class="brand__en">Maplewood<br>Kids Health<br>Centre</div>
  </header>
  <div class="contact-top">
    <div class="contact-line"><svg class="icon" viewBox="0 0 10 10"><path d="M2 0.5l2 2-1 1.2c.6 1.3 1.6 2.3 2.8 2.8L7 5.5l2 2-1.3 1.8C4.5 9 1 5.5 .5 2.2z"/></svg>(514) 555-0142</div>
    <div class="contact-line"><svg class="icon" viewBox="0 0 10 10"><path d="M2.2 2h5.6l1.2 3v3H8v1H6.8V8H3.2v1H2V8H1V5zm.6 1L2 5h6l-.8-2z"/></svg>(514) 555-0187</div>
  </div>

  <div class="staff-column">
    <p class="address">2250 boul. des Érables<br>Suite 100<br>Bellerive, Qc<br>H0H 2B5</p>
    <div class="contact-line"><svg class="icon" viewBox="0 0 10 10"><path d="M2 0.5l2 2-1 1.2c.6 1.3 1.6 2.3 2.8 2.8L7 5.5l2 2-1.3 1.8C4.5 9 1 5.5 .5 2.2z"/></svg>(514) 555-0142</div>
    <div class="contact-line"><svg class="icon" viewBox="0 0 10 10"><path d="M2.2 2h5.6l1.2 3v3H8v1H6.8V8H3.2v1H2V8H1V5zm.6 1L2 5h6l-.8-2z"/></svg>(514) 555-0187</div>

    <div class="dept" style="margin-top:10px"><p class="dept__title">Pédiatres / Pediatricians</p>
      <p class="dept__names">H. Lambert<br>J. Ferland<br>R. Castonguay<br>D. Gagnon<br>N. Bouchard<br>M. Perrault<br>D. Leclerc</p></div>
    <div class="dept"><p class="dept__title">Neurologue / Neurologist</p><p class="dept__names">M. Dufresne</p></div>
    <div class="dept"><p class="dept__title">O.R.L. / E.N.T.</p><p class="dept__names">T. Morin</p></div>
    <div class="dept"><p class="dept__title">Urologue / Urologist</p><p class="dept__names">R. Lavoie</p></div>
    <div class="dept"><p class="dept__title">Psychologues / Psychologists</p><p class="dept__names">H. Girard<br>A. Roy</p></div>
    <div class="dept"><p class="dept__title">Travailleuse social / Social worker</p><p class="dept__names">S. Pelletier</p></div>
    <div class="dept" style="margin-top:16px"><p class="dept__title">Gerante / Manager</p><p class="dept__names">C. Beaulieu</p></div>
  </div>

  <footer class="footer">
    <svg width="571" height="80" viewBox="0 0 571 80">
      <path d="M0 3 C40 30 120 40 260 36 C380 33 480 34 571 52 L571 80 L0 80 Z" fill="var(--brand-purple)"/>
      <path d="M0 33 C120 38 200 28 300 27 C420 26 500 36 571 49 L571 80 L0 80 Z" fill="#fff"/>
      <path d="M0 37 C120 42 200 32 300 31 C420 30 500 40 571 52 L571 80 L0 80 Z" fill="var(--brand-blue)"/>
    </svg>
    <p class="footer__address">2250 boul. des Érables, Suite 100, Bellerive, Qc, H0H 2B5</p>
  </footer>
</section>

<section class="sheet sheet--plain">
  <header class="brand">
    <div class="brand__fr">Centre<br>médical<br>Bellerive</div>
    <div class="brand__dot"></div>
    <div class="brand__en">Maplewood<br>Kids Health<br>Centre</div>
  </header>
  <div class="contact-top">
    <div class="contact-line"><svg class="icon" viewBox="0 0 10 10"><path d="M2 0.5l2 2-1 1.2c.6 1.3 1.6 2.3 2.8 2.8L7 5.5l2 2-1.3 1.8C4.5 9 1 5.5 .5 2.2z"/></svg>(514) 555-0142</div>
    <div class="contact-line"><svg class="icon" viewBox="0 0 10 10"><path d="M2.2 2h5.6l1.2 3v3H8v1H6.8V8H3.2v1H2V8H1V5zm.6 1L2 5h6l-.8-2z"/></svg>(514) 555-0187</div>
  </div>

  <footer class="footer">
    <svg width="571" height="80" viewBox="0 0 571 80">
      <path d="M0 3 C40 30 120 40 260 36 C380 33 480 34 571 52 L571 80 L0 80 Z" fill="var(--brand-purple)"/>
      <path d="M0 33 C120 38 200 28 300 27 C420 26 500 36 571 49 L571 80 L0 80 Z" fill="#fff"/>
      <path d="M0 37 C120 42 200 32 300 31 C420 30 500 40 571 52 L571 80 L0 80 Z" fill="var(--brand-blue)"/>
    </svg>
    <p class="footer__address">2250 boul. des Érables, Suite 100, Bellerive, Qc, H0H 2B5</p>
  </footer>
</section>

</body>
</html>
```